Criação de Layout Web-Design para Beleza
" Nossa empresa promove o embelezamento de nossos clientes com protocolos exclusivos adequados a cada cliente respeitando sempre suas singularidades. "

```html
<!DOCTYPE html>
<html lang="pt-BR">
<head>
<meta charset="UTF-8">
<title>Luana Serafim — Estética Avançada</title>
<link href="https://fonts.googleapis.com/css2?family=Montserrat:wght@400;500;600;700&family=Cormorant+Garamond:wght@500&display=swap" rel="stylesheet">
<style>
  :root {
    --page: #e9e9eb;
    --pink: #e8336f;
    --white: #ffffff;
    --ink: #2b2523;
    --muted: #8a8583;
    --photo-dark: #6f5443;
    --photo-mid: #a98066;
    --photo-light: #c9a48a;
    --nav-shade: rgba(30, 22, 18, 0.35);
  }
  * { box-sizing: border-box; margin: 0; padding: 0; }
  html, body { width: 1200px; height: 1200px; overflow: hidden; }
  body {
    background: var(--page);
    font-family: "Montserrat", sans-serif;
    color: var(--white);
    position: relative;
  }

  /* Desktop layout */
  .desktop {
    position: absolute; left: 40px; top: 250px;
    width: 800px; height: 500px;
    overflow: hidden; border-radius: 4px;
    box-shadow: 0 10px 30px rgba(0,0,0,0.12);
  }
  .hero-photo {
    position: absolute; inset: 0;
    background: linear-gradient(100deg, var(--photo-mid) 0%, var(--photo-light) 45%, var(--photo-mid) 75%, var(--photo-dark) 100%);
  }
  .desktop-nav {
    position: absolute; left: 0; right: 0; top: 0; height: 56px;
    background: var(--nav-shade);
    display: flex; align-items: center; padding: 0 22px; gap: 18px;
    font-size: 10px; font-weight: 600; letter-spacing: 0.06em;
  }
  .desktop-nav .link { text-transform: uppercase; }
  .nav-cta {
    background: var(--pink); padding: 6px 12px; border-radius: 3px;
    font-size: 9px; font-weight: 600;
  }
  .desktop-brand {
    margin-left: auto;
    font-family: "Cormorant Garamond", serif; font-size: 17px; font-weight: 500;
    letter-spacing: 0.12em; text-transform: uppercase;
  }
  .search-icon { margin-left: 40px; }

  .video-link {
    position: absolute; left: 28px; bottom: 70px;
    display: flex; align-items: center; gap: 10px;
    font-size: 9px; font-weight: 600; text-transform: uppercase; letter-spacing: 0.06em;
  }
  .play-btn {
    width: 30px; height: 30px; border-radius: 50%; background: var(--pink);
    display: flex; align-items: center; justify-content: center;
  }
  .slider-dots { position: absolute; display: flex; gap: 5px; }
  .slider-dots span { width: 6px; height: 6px; border-radius: 50%; background: rgba(255,255,255,0.5); }
  .slider-dots span.active { background: var(--white); }
  .desktop .slider-dots { left: 30px; bottom: 40px; }

  .chat-box {
    position: absolute; right: 26px; bottom: 80px; width: 190px;
    background: var(--white); color: var(--ink); border-radius: 4px;
    padding: 12px; font-size: 8px; line-height: 1.4;
    box-shadow: 0 6px 16px rgba(0,0,0,0.18);
  }
  .chat-title { color: var(--pink); font-weight: 700; font-size: 9px; margin-bottom: 4px; }
  .chat-text { color: var(--muted); margin-bottom: 8px; }
  .chat-input { border-top: 1px solid #e2dedd; padding-top: 6px; color: var(--muted); }
  .chat-toggle {
    position: absolute; right: 26px; bottom: 40px; width: 26px; height: 26px;
    border-radius: 4px; background: var(--ink);
    display: flex; align-items: center; justify-content: center;
  }

  /* Mobile layout */
  .mobile {
    position: absolute; left: 880px; top: 280px;
    width: 280px; height: 580px; overflow: hidden; border-radius: 18px;
    box-shadow: 0 10px 30px rgba(0,0,0,0.12);
  }
  .mobile-header {
    position: absolute; left: 0; right: 0; top: 0; padding-top: 26px;
    text-align: center;
  }
  .mobile-brand {
    font-family: "Cormorant Garamond", serif; font-size: 20px; font-weight: 500;
    letter-spacing: 0.1em; text-transform: uppercase;
  }
  .mobile-tagline { font-size: 8px; margin-top: 2px; letter-spacing: 0.04em; }
  .social-row { display: flex; justify-content: center; gap: 8px; margin-top: 14px; }
  .social-row span { width: 16px; height: 16px; border-radius: 50%; border: 1px solid rgba(255,255,255,0.8); }
  .menu-btn {
    position: absolute; right: 14px; top: 112px; width: 24px; height: 24px;
    background: var(--pink); border-radius: 3px;
    display: flex; align-items: center; justify-content: center;
  }
  .mobile-headline {
    position: absolute; left: 22px; top: 300px;
    font-size: 34px; font-weight: 700; line-height: 1.15;
  }
  .mobile .slider-dots { left: 110px; bottom: 90px; }
  .mobile-actions {
    position: absolute; left: 18px; right: 18px; bottom: 30px;
    display: flex; justify-content: space-between; align-items: center;
    font-size: 9px; font-weight: 600;
  }
  .btn-pill { background: var(--pink); padding: 8px 16px; border-radius: 16px; }
  .watch-link { display: flex; align-items: center; gap: 6px; }
  .watch-link .play-btn { width: 20px; height: 20px; }
</style>
</head>
<body>

  <section class="desktop">
    <div class="hero-photo" role="img" aria-label="Foto de um jovem sorridente com toalha na cabeça aplicando algodão no rosto"></div>

    <nav class="desktop-nav">
      <span class="link">Home</span>
      <span class="link">Quem somos</span>
      <span class="link">Serviços</span>
      <span class="link">Blog</span>
      <span class="link">Contato</span>
      <span class="link">Depoimentos</span>
      <span class="nav-cta">Saiba mais</span>
      <span class="desktop-brand">Luana Serafim</span>
      <svg class="search-icon" width="14" height="14" viewBox="0 0 14 14" fill="none" stroke="#fff" stroke-width="1.6">
        <circle cx="6" cy="6" r="4.5"/><line x1="9.3" y1="9.3" x2="13" y2="13"/>
      </svg>
    </nav>

    <div class="video-link">
      <span class="play-btn">
        <svg width="10" height="10" viewBox="0 0 10 10"><path d="M3 2 L8 5 L3 8 Z" fill="#fff"/></svg>
      </span>
      <span>Veja o vídeo</span>
    </div>
    <div class="slider-dots"><span class="active"></span><span></span><span></span><span></span></div>

    <aside class="chat-box">
      <p class="chat-title">Luana Serafim</p>
      <p class="chat-text">Agende sua avaliação e descubra o protocolo ideal para você.</p>
      <p class="chat-input">Digite sua mensagem</p>
    </aside>
    <span class="chat-toggle">
      <svg width="12" height="12" viewBox="0 0 12 12" fill="none" stroke="#fff" stroke-width="1.4"><rect x="1.5" y="2" width="9" height="7" rx="1"/><path d="M4 9 L3 11 L6 9"/></svg>
    </span>
  </section>

  <section class="mobile">
    <div class="hero-photo" role="img" aria-label="Foto de um jovem sorridente com toalha na cabeça"></div>

    <header class="mobile-header">
      <p class="mobile-brand">Luana Serafim</p>
      <p class="mobile-tagline">Especialista em Estética Avançada</p>
      <div class="social-row"><span></span><span></span><span></span><span></span><span></span><span></span></div>
    </header>
    <span class="menu-btn">
      <svg width="12" height="10" viewBox="0 0 12 10" stroke="#fff" stroke-width="1.6"><line x1="0" y1="1" x2="12" y2="1"/><line x1="0" y1="5" x2="12" y2="5"/><line x1="0" y1="9" x2="12" y2="9"/></svg>
    </span>

    <h1 class="mobile-headline">Viva<br>melhor e<br>mais feliz!</h1>

    <div class="slider-dots"><span></span><span class="active"></span><span></span><span></span></div>

    <div class="mobile-actions">
      <span class="btn-pill">Agende já</span>
      <span class="watch-link">
        <span class="play-btn"><svg width="8" height="8" viewBox="0 0 10 10"><path d="M3 2 L8 5 L3 8 Z" fill="#fff"/></svg></span>
        Assista
      </span>
    </div>
  </section>

</body>
</html>
```